依頼詳細
コンセプトは「選べる婚活スタイル」です。
①仲人型婚活、②婚活パーティー運営、の2本柱がウリとなります。
ターゲットは20代後半~30代の女性、30代~40代前半の男性です。

色は下記のサイトを参考に
「色数少なめ」「白ベース」「サブカラーにゴールド」
を使用してください。
https://boutique.fenolu.jp/
http://quillmerdon.com/

▼ロゴは下記からダウンロードしてご利用ください。
http://16.bunkobox.nu/0118-a72cd40b9114ea8731811acf9e62c5b3d7

▼写真は下記からダウンロードしてご利用ください。
http://16.bunkobox.nu/0118-m58146b836c907d628221c7316b52e8c3

・スライドショーの部分に「top_slide.jpg」を利用してください。
・「婚活カウンセラー」の部分に「counselor.jpg」を利用してください。
・その他の写真に関しては特に指定はありません。
・フリーの写真素材で良いものがあれば、ご提案願います。(スライドショーの残り3パターン等)
サイトURL
https://selumia.jp/
ページ数
2ページ
希望イメージ
• +5 0 +5
• シンプル
複雑
• 単色
カラフル
• 暗い
明るい
• 日常
高級
• 遊び心
厳粛
• 未来的
伝統的
• 女性的
男性的
納品ファイル
• 高解像度JPG (.jpg)
• イラストレーター形式 (.ai)
• フォトショップ形式 (.psd)
• PNG形式 (.png)
補足説明
シンプルなデザインのサイトのため、バナー等のデザインクオリティがポイントになってくると思います。
----------
・「SELUMIAは成婚主義の結婚相談所です!」の図
・「SELUMIAの3つの特徴」の図
・「初めての方へ」バナー
・「会員数/実績データ」バナー
・「ご成婚までの流れ」バナー
----------
宜しくお願い致します。
依頼公開後の追記内容
ワイヤーフレームに
スライドショーエリアのキャッチコピーを追加しました。
-----------------------------------------------------
多くの結婚式をプロデュースしてきたルシェバルが
あなたの婚活を完全サポート

わたし達だから知っている ‘成婚の法則’
応募くださったランサーの皆様
素敵なデザインのご提案ありがとうございます。

現在、応募案の選定を検討しておりますが、
選定にしばらく時間がかかりそうなため、
その間も応募を受付させていただきます。

新たなアイデア等、ありましたらご提案いただければ幸いです。
引き続きよろしくお願いいたします。
トップページに表示する具体的なテキスト文章が用意できましたので

```html
<!DOCTYPE html>
<html lang="ja">
<head>
<meta charset="utf-8">
<title>SELUMIA | 結婚相談所</title>
<link href="https://fonts.googleapis.com/css2?family=Noto+Serif+JP:wght@400;600&family=Noto+Sans+JP:wght@400;500&family=Great+Vibes&family=Cormorant+Garamond:wght@500;600&display=swap" rel="stylesheet">
<style>
:root{
  --gold:#b59b63;
  --gold-light:#d8c69d;
  --gold-pale:#f3ecdc;
  --ink:#4f4337;
  --ink-soft:#8a7d70;
  --line:#e4dccd;
  --beige:#f5f1ea;
  --pink:#e9b7c0;
  --pink-pale:#fbf1f2;
  --footer:#6d645a;
  --link:#3b5a8c;
  --white:#ffffff;
}
*{box-sizing:border-box;margin:0;padding:0}
html,body{width:1200px;height:4912px;overflow:hidden}
body{background:var(--white);color:var(--ink);font-family:"Noto Sans JP",sans-serif;font-size:13px;line-height:1.8}
.wrap{width:900px;margin:0 auto;position:relative}
.ph{display:block}
.script{font-family:"Great Vibes",cursive;color:var(--gold);font-size:38px;line-height:1;font-weight:400}
.sec-head{text-align:center}
.sec-head .sub{font-family:"Noto Serif JP",serif;font-size:12px;color:var(--ink-soft);letter-spacing:.1em;margin-top:6px}
.btn{display:inline-block;background:var(--gold);color:var(--white);font-family:"Noto Serif JP",serif;font-size:13px;padding:10px 0;width:220px;text-align:center;letter-spacing:.1em}
.btn-line{background:var(--white);border:1px solid var(--gold);color:var(--gold)}

/* header */
.site-header{height:60px;border-bottom:1px solid var(--line);display:flex;align-items:center;padding:0 60px;justify-content:space-between}
.logo{display:flex;align-items:center;gap:8px;font-family:"Cormorant Garamond",serif;font-size:26px;font-weight:600;color:var(--gold);letter-spacing:.08em}
.logo-dot{width:10px;height:10px;border-radius:50%;background:var(--gold)}
.logo small{font-family:"Noto Sans JP",sans-serif;font-size:10px;color:var(--ink-soft);letter-spacing:.05em;font-weight:400;margin-left:6px}
.gnav{display:flex}
.gnav a{display:block;padding:0 16px;text-align:center;border-left:1px solid var(--line);font-family:"Cormorant Garamond",serif;font-size:13px;font-weight:600;color:var(--ink);line-height:1.3;text-decoration:none}
.gnav a:last-child{border-right:1px solid var(--line)}
.gnav a span{display:block;font-family:"Noto Sans JP",sans-serif;font-size:9px;color:var(--ink-soft);font-weight:400}
.head-contact{text-align:right;font-size:10px;color:var(--ink-soft);line-height:1.5}
.head-contact .tel{font-family:"Cormorant Garamond",serif;font-size:17px;color:var(--gold);font-weight:600}
.head-btns{display:flex;gap:4px;margin-top:3px}
.head-btns span{display:block;font-size:9px;color:var(--white);padding:2px 10px;background:var(--pink)}
.head-btns span+span{background:var(--gold)}

/* hero */
.hero{height:580px;position:relative}
.hero-photo{width:1200px;height:540px;background:linear-gradient(180deg,#efe9e2 0%,#d9d0c7 55%,#b7aca2 100%)}
.hero-catch{position:absolute;top:26px;left:270px;width:660px;background:rgba(255,255,255,.92);border-top:2px solid var(--gold);border-bottom:2px solid var(--gold);text-align:center;padding:10px 0 12px}
.hero-catch p{font-family:"Noto Serif JP",serif;font-size:13px;color:var(--ink-soft)}
.hero-catch h1{font-family:"Noto Serif JP",serif;font-weight:600;font-size:30px;color:var(--ink);letter-spacing:.06em;line-height:1.5}
.hero-catch h1 em{font-style:normal;color:var(--gold)}
.dots{display:flex;gap:10px;justify-content:center;height:40px;align-items:center}
.dots i{width:8px;height:8px;border-radius:50%;background:var(--line)}
.dots i:first-child{background:var(--gold)}

/* info + policy */
.info{height:330px;padding-top:30px}
.info .wrap{display:flex;justify-content:space-between}
.news{width:400px}
.news .sec-head{margin-bottom:18px;border-bottom:1px solid var(--line);padding-bottom:10px}
.news li{list-style:none;display:flex;gap:18px;font-size:12px;border-bottom:1px dotted var(--line);padding:7px 0}
.news time{color:var(--gold);font-family:"Cormorant Garamond",serif;font-size:14px;font-weight:600}
.policy{width:450px;border:1px solid var(--gold-light);padding:22px 24px;text-align:center;position:relative}
.policy .label{font-family:"Cormorant Garamond",serif;color:var(--gold);font-size:13px;letter-spacing:.2em;font-weight:600}
.policy h2{font-family:"Noto Serif JP",serif;font-size:16px;font-weight:600;margin:4px 0 20px;border-bottom:1px solid var(--gold);display:inline-block;padding:0 6px 2px}
.policy h2 b{color:var(--gold);font-size:19px}
.steps{display:flex;justify-content:space-between;align-items:center}
.step{width:78px;text-align:center;font-size:11px}
.step i{display:flex;width:66px;height:66px;margin:0 auto 6px;border-radius:50%;border:1px solid var(--gold-light);align-items:center;justify-content:center;font-family:"Cormorant Garamond",serif;font-style:normal;font-size:24px;color:var(--gold);font-weight:600}
.step.goal i{background:var(--gold);color:var(--white);border-color:var(--gold)}
.step.goal{color:var(--gold);font-weight:500}

/* features */
.features{height:720px;background:linear-gradient(180deg,#fbeef0 0%,#fff 100%);padding-top:40px}
.features .sec-head h2{font-family:"Noto Serif JP",serif;font-size:18px;font-weight:600;margin-top:8px}
.features .sec-head h2 b{color:var(--gold);font-size:24px}
.feat-body{display:flex;justify-content:space-between;margin-top:30px}
.feat-list{width:430px;display:flex;flex-direction:column;gap:16px}
.feat{background:var(--white);border:1px solid var(--line)}
.feat h3{font-family:"Noto Serif JP",serif;font-size:15px;font-weight:600;padding:8px 14px;border-bottom:1px solid var(--gold-light);display:flex;gap:10px;align-items:center}
.feat h3 span{width:26px;height:26px;background:var(--gold);color:var(--white);display:flex;align-items:center;justify-content:center;font-family:"Cormorant Garamond",serif;font-size:16px}
.feat .in{display:flex;gap:14px;padding:12px 14px;font-size:11px;line-height:1.75}
.feat .in .ph{width:150px;height:100px;flex:none}
.feat-side{width:430px;font-size:12px;line-height:2}
.feat-side p+p{margin-top:14px}
.rings{width:430px;height:240px;margin-top:30px;background:radial-gradient(ellipse at 55% 55%,#efe6d8 0%,#f7f2ec 60%,#fbf7f4 100%)}

/* select style */
.select{height:580px;padding-top:40px}
.styles{display:flex;justify-content:space-between;margin-top:30px}
.style{width:420px;text-align:center}
.style .ico{width:130px;height:130px;border-radius:50%;margin:0 auto;background:radial-gradient(circle,#fff 0%,#f2e9d6 70%,#e7d9ba 100%);border:1px solid var(--gold-light)}
.style h3{font-family:"Noto Serif JP",serif;font-size:16px;font-weight:600;color:var(--gold);margin:12px 0 4px}
.style .en{font-family:"Cormorant Garamond",serif;font-size:11px;letter-spacing:.2em;color:var(--ink-soft);margin-top:10px}
.style p{text-align:left;font-size:12px;line-height:2;margin:16px 0 24px;height:150px}

/* banners */
.banners{height:260px;background:var(--beige);padding-top:40px}
.banners .wrap{display:flex;justify-content:space-between}
.banner{width:288px;height:180px;background:var(--white);padding:6px;position:relative}
.banner .ph{height:120px}
.banner .cap{text-align:center;padding-top:6px}
.banner .cap b{display:block;font-family:"Cormorant Garamond",serif;font-size:17px;color:var(--gold);letter-spacing:.2em;line-height:1.2}
.banner .cap span{font-size:11px;color:var(--ink-soft)}

/* blog faq */
.bf{height:700px;padding-top:50px}
.bf .wrap{display:flex;justify-content:space-between}
.col{width:430px}
.col .sec-head{margin-bottom:20px}
.blog-item{display:flex;gap:14px;padding:12px 0;border-bottom:1px dotted var(--line)}
.blog-item .ph{width:90px;height:68px;flex:none}
.blog-item time{display:block;font-family:"Cormorant Garamond",serif;color:var(--gold);font-size:13px;font-weight:600;line-height:1.4}
.blog-item p{font-size:12px}
.faq-item{padding:12px 0;border-bottom:1px dotted var(--line)}
.faq-item dt{display:flex;gap:10px;font-weight:500;font-size:13px}
.faq-item dd{display:flex;gap:10px;font-size:11px;color:var(--ink-soft);margin-top:4px}
.qa{width:20px;height:20px;flex:none;border-radius:50%;background:var(--gold);color:var(--white);font-family:"Cormorant Garamond",serif;font-size:13px;display:flex;align-items:center;justify-content:center;line-height:1}
.qa.a{background:var(--pink)}
.more{text-align:center;margin-top:26px}

/* sns counselor */
.sc{height:800px;padding-top:40px}
.sc .wrap{display:flex;justify-content:space-between}
.feed{width:340px;height:640px;border:1px solid var(--line);overflow:hidden}
.feed .cover{height:120px;background:linear-gradient(135deg,#eadfd2,#d7c9bb)}
.feed .page{display:flex;gap:10px;padding:10px;border-bottom:1px solid var(--line)}
.feed .page i{width:44px;height:44px;background:var(--gold-pale);border:1px solid var(--line);flex:none}
.feed .page b{font-size:13px;color:var(--link);font-weight:500}
.feed .page span{display:block;font-size:10px;color:var(--ink-soft)}
.post{padding:12px;border-bottom:1px solid var(--line);font-size:11px}
.post b{font-size:12px;color:var(--link);font-weight:500}
.post .ph{height:110px;margin-top:8px}
.counselor{width:520px;border:1px solid var(--gold-light);padding:28px 30px;position:relative;height:640px}
.counselor .top{display:flex;gap:20px;align-items:flex-end;border-bottom:1px solid var(--line);padding-bottom:14px}
.counselor .top .sub{font-size:11px;color:var(--ink-soft);font-family:"Noto Serif JP",serif}
.counselor .name{font-family:"Noto Serif JP",serif;font-size:18px;font-weight:600}
.counselor .name small{font-size:11px;color:var(--gold);margin-right:10px;font-weight:400}
.counselor .body{display:flex;gap:20px;margin-top:20px}
.counselor .body p{font-size:12px;line-height:2.1}
.counselor .body p+p{margin-top:12px}
.counselor .photo{width:170px;height:230px;flex:none;background:linear-gradient(180deg,#efe8e1,#cfc3b7)}

/* access */
.access{height:560px;padding-top:40px;background:linear-gradient(180deg,#fff 0%,var(--beige) 100%)}
.access .body{display:flex;justify-content:space-between;margin-top:26px}
.access-info{width:300px}
.access-info .logo{font-size:22px}
.access-info dl{margin-top:14px;font-size:12px}
.access-info dt{color:var(--gold);font-family:"Cormorant Garamond",serif;font-weight:600;letter-spacing:.15em;font-size:12px;margin-top:10px}
.access-info .tel{font-family:"Cormorant Garamond",serif;font-size:24px;font-weight:600;color:var(--ink);display:flex;align-items:center;gap:6px}
.access-info .btns{display:flex;gap:10px;margin-top:22px}
.access-info .btns .btn{width:140px;font-size:11px}
.map{width:570px;height:380px;background:linear-gradient(135deg,#eeebe6,#e0dcd5)}

/* footer */
.site-footer{height:250px;background:var(--footer);color:#efe9e0;padding-top:26px}
.fnav{display:flex;flex-wrap:wrap;justify-content:center;gap:4px 26px;font-size:11px;width:900px;margin:0 auto}
.fnav span::before{content:"›";margin-right:5px;color:var(--gold-light)}
.fbody{display:flex;justify-content:center;align-items:center;gap:40px;margin-top:34px;border-top:1px solid #867c71;padding-top:26px;width:900px;margin-left:auto;margin-right:auto}
.fbody .logo{color:#f2e9d7}
.fbody .logo-dot{background:#f2e9d7}
.fbody p{font-size:11px;line-height:1.8}
.fbody .tel{font-family:"Cormorant Garamond",serif;font-size:22px;font-weight:600}
.bottom{height:72px;display:flex;align-items:center;justify-content:space-between;padding:0 150px;background:var(--white)}
.badge{display:flex;align-items:center;gap:10px;font-family:"Noto Serif JP",serif;font-size:14px;font-weight:600}
.badge i{width:34px;height:34px;background:var(--gold-pale);border:1px solid var(--gold-light)}
.copy{font-size:10px;color:var(--ink-soft);font-family:"Cormorant Garamond",serif;letter-spacing:.1em}
</style>
</head>
<body>

<header class="site-header">
  <div class="logo"><span class="logo-dot"></span>SELUMIA<small>ブライダルサロン セルミア</small></div>
  <nav class="gnav">
    <a>ABOUT<span>初めての方へ</span></a>
    <a>DATA<span>会員数・実績</span></a>
    <a>FLOW<span>ご成婚までの流れ</span></a>
    <a>BLOG<span>ブログ</span></a>
    <a>ACCESS<span>アクセス</span></a>
    <a>FAQ<span>よくある質問</span></a>
  </nav>
  <div class="head-contact">
    <div><span class="tel">027-555-0182</span> 受付 10:00〜19:00</div>
    <div class="head-btns"><span>無料カウンセリング予約</span><span>資料請求はこちら</span></div>
  </div>
</header>

<section class="hero">
  <div class="hero-photo ph" role="img" aria-label="黒いスーツ姿のスタッフ7名が並ぶサロンの集合写真"></div>
  <div class="hero-catch">
    <p>多くの結婚式をプロデュースしてきた私たちがあなたの婚活を完全サポート</p>
    <h1>わたし達だから知っている<em>“成婚の法則”</em></h1>
  </div>
  <div class="dots"><i></i><i></i><i></i><i></i></div>
</section>

<section class="info">
  <div class="wrap">
    <div class="news">
      <div class="sec-head"><div class="script">Information</div><div class="sub">お知らせ</div></div>
      <ul>
        <li><time>2016.01.17</time>春の婚活パーティー日程を公開しました</li>
        <li><time>2016.01.12</time>無料カウンセリングの受付時間を変更しました</li>
        <li><time>2016.01.08</time>1月のご成婚カップルをご紹介します</li>
        <li><time>2016.01.04</time>年始のご挨拶と営業日のお知らせ</li>
        <li><time>2015.12.25</time>冬季休業期間についてのお知らせ</li>
      </ul>
    </div>
    <div class="policy">
      <div class="label">OUR POLICY</div>
      <h2><b>SELUMIA</b>は成婚主義の結婚相談所です！</h2>
      <div class="steps">
        <div class="step"><i>1</i>出会い</div>
        <svg width="14" height="14" viewBox="0 0 14 14"><path d="M3 1l7 6-7 6" fill="none" stroke="#b59b63" stroke-width="1.5"/></svg>
        <div class="step"><i>2</i>お見合い</div>
        <svg width="14" height="14" viewBox="0 0 14 14"><path d="M3 1l7 6-7 6" fill="none" stroke="#b59b63" stroke-width="1.5"/></svg>
        <div class="step"><i>3</i>交際</div>
        <svg width="14" height="14" viewBox="0 0 14 14"><path d="M3 1l7 6-7 6" fill="none" stroke="#b59b63" stroke-width="1.5"/></svg>
        <div class="step goal"><i>4</i>結婚</div>
      </div>
    </div>
  </div>
</section>

<section class="features">
  <div class="wrap">
    <div class="sec-head">
      <div class="script">Marriage Producer SELUMIA</div>
      <h2><b>SELUMIA</b>の<b>3</b>つの特徴</h2>
    </div>
    <div class="feat-body">
      <div class="feat-list">
        <div class="feat">
          <h3><span>1</span>徹底したカウンセリング</h3>
          <div class="in"><div class="ph" role="img" aria-label="笑顔で相談に応じる女性カウンセラーの写真" style="background:linear-gradient(135deg,#f1e6e1,#dccbc1)"></div><p>入会前から専任カウンセラーが丁寧にお話を伺います。お一人おひとりの価値観や理想を理解し、最適な出会いをご提案します。</p></div>
        </div>
        <div class="feat">
          <h3><span>2</span>多彩な婚活プランをご提案</h3>
          <div class="in"><div class="ph" role="img" aria-label="タブレットでプランを説明する手元の写真" style="background:linear-gradient(135deg,#eeeae4,#d6cfc4)"></div><p>仲人型のお見合いと婚活パーティーを組み合わせ、ライフスタイルに合わせた無理のない婚活プランをお作りします。</p></div>
        </div>
        <div class="feat">
          <h3><span>3</span>二人三脚で「成婚」にこだわります</h3>
          <div class="in"><div class="ph" role="img" aria-label="並んで歩く新郎新婦の写真" style="background:linear-gradient(135deg,#f3ece6,#ddd2c8)"></div><p>交際中の悩みや不安にも寄り添い、ご成婚まで一緒に歩みます。結婚式をよく知る私たちだからこその支えがあります。</p></div>
        </div>
      </div>
      <div class="feat-side">
        <p>SELUMIAは結婚相談所です。ブライダルの現場で数多くの結婚式をお手伝いしてきた経験から、幸せなご夫婦の共通点を知っています。</p>
        <p>出会いから交際、そしてご成婚まで。私たちは「出会わせて終わり」ではなく、お二人が結ばれるその日まで責任を持ってサポートいたします。</p>
        <p>お見合いに不安がある方も、パーティーで気軽に出会いたい方も、まずはお気軽に無料カウンセリングへお越しください。</p>
        <div class="rings ph" role="img" aria-label="重なり合うゴールドとプラチナの結婚指輪の写真"></div>
      </div>
    </div>
  </div>
</section>

<section class="select">
  <div class="wrap">
    <div class="sec-head"><div class="script">Select Style</div><div class="sub">選べる婚活スタイル</div></div>
    <div class="styles">
      <div class="style">
        <div class="ico ph" role="img" aria-label="乾杯するグラスのイラスト"></div>
        <div class="en">PARTY</div>
        <h3>パーティ型婚活スタイル</h3>
        <p>気軽に参加できる少人数制の婚活パーティーを定期開催しています。スタッフが会話のきっかけ作りをお手伝いするので、初めての方も安心です。趣味や年代別のテーマパーティーもご用意。自然な雰囲気の中で、素敵なお相手との出会いを楽しんでください。</p>
        <span class="btn">詳しくはこちら</span>
      </div>
      <div class="style">
        <div class="ico ph" role="img" aria-label="寄り添う二人のイラスト"></div>
        <div class="en">MATCHMAKING</div>
        <h3>仲人型婚活スタイル</h3>
        <p>専任の仲人があなたの希望や価値観を丁寧に伺い、相性の良いお相手をご紹介します。お見合いのセッティングから交際中のアドバイス、プロポーズのご相談まで一貫してサポート。真剣に結婚を考える方のための、安心の婚活スタイルです。</p>
        <span class="btn">詳しくはこちら</span>
      </div>
    </div>
  </div>
</section>

<section class="banners">
  <div class="wrap">
    <div class="banner"><div class="ph" role="img" aria-label="白い花のブーケの写真" style="background:linear-gradient(135deg,#f4f1ec,#e2dbd0)"></div><div class="cap"><b>ABOUT</b><span>初めての方へ</span></div></div>
    <div class="banner"><div class="ph" role="img" aria-label="手を取り合う新郎新婦の写真" style="background:linear-gradient(135deg,#e8e2db,#c9bdb0)"></div><div class="cap"><b>DATA</b><span>会員数・実績データ</span></div></div>
    <div class="banner"><div class="ph" role="img" aria-label="式場のチャペルの写真" style="background:linear-gradient(135deg,#efe9e3,#d4c6b6)"></div><div class="cap"><b>FLOW</b><span>ご成婚までの流れ</span></div></div>
  </div>
</section>

<section class="bf">
  <div class="wrap">
    <div class="col">
      <div class="sec-head"><div class="script">Blog</div><div class="sub">ブログ</div></div>
      <div class="blog-item"><div class="ph" role="img" aria-label="カフェの写真" style="background:#e9e0d6"></div><div><time>2016.01.17</time><p>初めてのお見合いで気をつけたいポイント</p></div></div>
      <div class="blog-item"><div class="ph" role="img" aria-label="パーティー会場の写真" style="background:#e5ddd2"></div><div><time>2016.01.14</time><p>先週末の婚活パーティーは大盛況でした！次回の募集もスタート</p></div></div>
      <div class="blog-item"><div class="ph" role="img" aria-label="花束の写真" style="background:#efe6e3"></div><div><time>2016.01.10</time><p>ご成婚退会されたお二人からのメッセージ</p></div></div>
      <div class="blog-item"><div class="ph" role="img" aria-label="指輪の写真" style="background:#ece5da"></div><div><time>2016.01.06</time><p>「カフェ婚活」が人気の理由とは？スタッフがご紹介します</p></div></div>
      <div class="more"><span class="btn btn-line">MORE</span></div>
    </div>
    <div class="col">
      <div class="sec-head"><div class="script">FAQ</div><div class="sub">よくある質問</div></div>
      <dl>
        <div class="faq-item"><dt><span class="qa">Q</span>結婚相談所に通うのは初めてで不安です。</dt><dd><span class="qa a">A</span>専任カウンセラーが最初から丁寧にご案内しますのでご安心ください。</dd></div>
        <div class="faq-item"><dt><span class="qa">Q</span>どんな会員が登録していますか？</dt><dd><span class="qa a">A</span>20代後半から40代の真剣に結婚を考える方が中心です。</dd></div>
        <div class="faq-item"><dt><span class="qa">Q</span>仕事が忙しくても活動できますか？</dt><dd><span class="qa a">A</span>ご都合に合わせた日程調整やオンライン相談も可能です。</dd></div>
        <div class="faq-item"><dt><span class="qa">Q</span>パーティーだけの参加もできますか？</dt><dd><span class="qa a">A</span>はい、どなたでもご参加いただけます。</dd></div>
      </dl>
      <div class="more"><span class="btn btn-line">MORE</span></div>
    </div>
  </div>
</section>

<section class="sc">
  <div class="wrap">
    <div class="feed">
      <div class="cover ph" role="img" aria-label="サロン店内の写真"></div>
      <div class="page"><i></i><div><b>婚活サポートSELUMIA (セルミア)</b><span>1,240人が「いいね！」しています</span></div></div>
      <div class="post"><b>婚活サポートSELUMIA (セルミア)</b><p>【2月の婚活パーティー】参加者募集中です！今回は少人数制のカフェパーティー。お気軽にご参加ください。</p><div class="ph" role="img" aria-label="パーティー会場の写真" style="background:linear-gradient(135deg,#ede6de,#d9cdc0)"></div></div>
      <div class="post"><b>婚活サポートSELUMIA (セルミア)</b><p>今月もご成婚のご報告をいただきました。おめでとうございます。</p></div>
    </div>
    <div class="counselor">
      <div class="top">
        <div><div class="script">Counselor</div><div class="sub">婚活カウンセラー紹介</div></div>
        <div class="name"><small>婚活カウンセラー</small>藤田 さやか</div>
      </div>
      <div class="body">
        <div>
          <p>ブライダルの仕事に携わって十年以上、多くの新郎新婦様の晴れの日をお手伝いしてまいりました。</p>
          <p>幸せなご夫婦を見てきたからこそ分かる「成婚のヒント」を、皆さまの婚活に活かしたいと考えています。</p>
          <p>婚活は不安もつきものですが、一人で悩まずに何でもご相談ください。あなたらしい幸せのかたちを、一緒に見つけていきましょう。</p>
          <p>お会いできる日を心より楽しみにしております。</p>
        </div>
        <div class="photo ph" role="img" aria-label="黒いスーツ姿の女性カウンセラーの写真"></div>
      </div>
    </div>
  </div>
</section>

<section class="access">
  <div class="wrap">
    <div class="sec-head"><div class="script">Access Map</div><div class="sub">アクセス</div></div>
    <div class="body">
      <div class="access-info">
        <div class="logo"><span class="logo-dot"></span>SELUMIA</div>
        <dl>
          <dt>ADDRESS</dt><dd>〒370-0000 架空県青葉市緑町2-14-8<br>グリーンテラス3F</dd>
          <dt>TEL</dt><dd class="tel"><svg width="16" height="16" viewBox="0 0 24 24"><path d="M6.6 10.8c1.4 2.8 3.8 5.1 6.6 6.6l2.2-2.2c.3-.3.7-.4 1-.2 1.1.4 2.3.6 3.6.6.6 0 1 .4 1 1V20c0 .6-.4 1-1 1C10.6 21 3 13.4 3 4c0-.6.4-1 1-1h3.5c.6 0 1 .4 1 1 0 1.3.2 2.5.6 3.6.1.3 0 .7-.2 1L6.6 10.8z" fill="#b59b63"/></svg>027-555-0182</dd>
          <dt>OPEN</dt><dd>11:00〜19:00</dd>
          <dt>HOLIDAY</dt><dd>毎週火曜日</dd>
        </dl>
        <div class="btns"><span class="btn">お問い合わせ</span><span class="btn btn-line">資料請求</span></div>
      </div>
      <div class="map ph" role="img" aria-label="サロン周辺の地図"></div>
    </div>
  </div>
</section>

<footer class="site-footer">
  <nav class="fnav">
    <span>トップ</span><span>初めての方へ</span><span>会員数・実績データ</span><span>ご成婚までの流れ</span><span>パーティ型婚活</span><span>仲人型婚活</span><span>料金プラン</span><span>ブログ</span><span>よくある質問</span><span>アクセス</span><span>お問い合わせ</span><span>プライバシーポリシー</span>
  </nav>
  <div class="fbody">
    <div class="logo"><span class="logo-dot"></span>SELUMIA</div>
    <p>〒370-0000 架空県青葉市緑町2-14-8 グリーンテラス3F<br>営業時間 11:00〜19:00 ／ 定休日 毎週火曜日</p>
    <div class="tel">027-555-0182</div>
  </div>
</footer>
<div class="bottom">
  <div class="badge"><i></i>全国結婚相談ネットワーク 加盟店</div>
  <div class="copy">© SELUMIA Marriage Producer. All Rights Reserved.</div>
</div>

</body>
</html>
```